Forest Consultant/Timber Buyer needs a clean business card

We are a forestry consulting and timber buying company. We meet with private landowners and assist them with timber management and timber harvesting. We would like a professional business card, please no clip art. logo is blue and white but would like to see a gray,silver, or some other color incorporated. Would like basic contact info. Would like to the layout to be creative and sleek but masculine.

Target Market(s)

private landowners

Industry/Entity Type

Business

Contact Information for Business Card

name,position, cell number, office number, email, website. This might be to cluttered. Basic contact info is what we are looking for.

Contact info can all be on one side with logo on the other.

Font styles to use
Serif
Sans Serif

Colors
0255a3
ffffff
aaaaaa

Requirements
Must have
• We just want it professional.
Nice to have
• Creative layout.
Should not have
• please no clip art of log trucks etc.

```html
<!DOCTYPE html>
<html lang="en">
<head>
<meta charset="utf-8">
<title>Stonecrest Land &amp; Timber — Business Card</title>
<link rel="stylesheet" href="https://fonts.googleapis.com/css2?family=Open+Sans:wght@400;600;700&display=swap">
<style>
  :root {
    --brand-blue: #0255a3;
    --card-back-blue: #0f4f9a;
    --card-back-blue-light: #1a5ba6;
    --paper: #ffffff;
    --ink: #444444;
    --ink-strong: #555555;
    --stage: #e4e4e4;
    --shadow: rgba(0, 0, 0, 0.35);
  }
  * { margin: 0; padding: 0; box-sizing: border-box; }
  html, body {
    width: 1200px;
    height: 1000px;
    overflow: hidden;
    background: var(--stage);
    font-family: "Open Sans", Arial, sans-serif;
  }
  .stage {
    position: relative;
    width: 1200px;
    height: 1000px;
  }
  .card {
    position: absolute;
    left: 265px;
    width: 666px;
    height: 397px;
    box-shadow: 0 3px 8px var(--shadow);
    overflow: hidden;
  }
  .card--front { top: 73px; background: var(--paper); }
  .card--back { top: 533px; background: var(--card-back-blue); }

  .brand {
    position: absolute;
    display: flex;
    align-items: center;
    gap: 22px;
  }
  .card--front .brand { left: 108px; top: 78px; }
  .card--back .brand { left: 108px; top: 150px; }
  .brand__dot {
    width: 110px;
    height: 110px;
    border-radius: 50%;
    flex: none;
  }
  .brand__name {
    font-weight: 700;
    line-height: 1;
  }
  .brand__main {
    display: block;
    font-size: 50px;
    letter-spacing: 1px;
  }
  .brand__sub {
    display: block;
    margin-top: 14px;
    margin-left: 34px;
    font-size: 17px;
    letter-spacing: 3.5px;
  }
  .card--front .brand__dot { background: var(--brand-blue); }
  .card--front .brand__name { color: var(--brand-blue); }
  .card--back .brand__dot { background: var(--paper); }
  .card--back .brand__name { color: var(--paper); }

  .person {
    position: absolute;
    right: 352px;
    top: 281px;
    text-align: right;
  }
  .person__name {
    font-size: 19px;
    font-weight: 700;
    color: var(--ink-strong);
  }
  .person__title {
    margin-top: 2px;
    font-size: 16px;
    color: var(--brand-blue);
  }

  .contact {
    position: absolute;
    left: 349px;
    top: 270px;
    list-style: none;
  }
  .contact__item {
    display: flex;
    align-items: center;
    gap: 8px;
    height: 25px;
    font-size: 16px;
    color: var(--ink);
  }
  .contact__icon { width: 15px; height: 15px; flex: none; }

  .card__pattern {
    position: absolute;
    inset: 0;
    background: linear-gradient(180deg, var(--card-back-blue-light), var(--card-back-blue));
  }
</style>
</head>
<body>
<main class="stage">

  <section class="card card--front" aria-label="Business card, front">
    <div class="brand">
      <span class="brand__dot"></span>
      <p class="brand__name">
        <span class="brand__main">STONECREST</span>
        <span class="brand__sub">LAND &amp; TIMBER</span>
      </p>
    </div>

    <div class="person">
      <p class="person__name">Daniel Whitmore</p>
      <p class="person__title">Management Consultant</p>
    </div>

    <ul class="contact">
      <li class="contact__item">
        <svg class="contact__icon" viewBox="0 0 15 15" aria-hidden="true">
          <rect x="4" y="0.5" width="7" height="14" rx="1.2" fill="none" stroke="#0255a3" stroke-width="1.3"/>
          <rect x="5.5" y="2.5" width="4" height="6" fill="#0255a3"/>
          <circle cx="7.5" cy="11.8" r="0.9" fill="#0255a3"/>
        </svg>
        <span>+ 000 000 0000</span>
      </li>
      <li class="contact__item">
        <svg class="contact__icon" viewBox="0 0 15 15" aria-hidden="true">
          <rect x="0.5" y="3" width="14" height="9.5" fill="#0255a3"/>
          <path d="M0.8 3.3 L7.5 8.5 L14.2 3.3" fill="none" stroke="#ffffff" stroke-width="1.2"/>
        </svg>
        <span>info@stonecrestland.com</span>
      </li>
      <li class="contact__item">
        <svg class="contact__icon" viewBox="0 0 15 15" aria-hidden="true">
          <circle cx="6.5" cy="6.5" r="5.8" fill="none" stroke="#0255a3" stroke-width="1.3"/>
          <path d="M0.8 6.5 H12.2 M6.5 0.8 C3.8 4 3.8 9 6.5 12.2 M6.5 0.8 C9.2 4 9.2 9 6.5 12.2" fill="none" stroke="#0255a3" stroke-width="1"/>
          <path d="M8 8 L14.5 10.5 L11.5 11.5 L10.5 14.5 Z" fill="#0255a3"/>
        </svg>
        <span>stonecrestland.com</span>
      </li>
    </ul>
  </section>

  <section class="card card--back" aria-label="Business card, back">
    <div class="card__pattern" role="img" aria-label="Faint repeating pattern of evergreen trees in a lighter blue"></div>
    <div class="brand">
      <span class="brand__dot"></span>
      <p class="brand__name">
        <span class="brand__main">STONECREST</span>
        <span class="brand__sub">LAND &amp; TIMBER</span>
      </p>
    </div>
  </section>

</main>
</body>
</html>
```